"The Craft of Patron Care," fourth edition cover design

Later this year, my publisher, Harold Brenton & Co., will issue a fourth, substantially revised edition of "The Craft of Patron Care," following the 2016 publication of the third edition and the second and first versions that were issued earlier.

To distinguish this new edition from previous ones, I need a cover design that visually connects and is consistent with what has preceded it, while signaling this is a new and different, worthy of prospective readers/buyers’ attention.

Attached are three different verbal approaches to the new cover; these are NOT MEANT to serve as actual designs, but rather will give you a sense of how language is to be deployed:

The first emphasizes “ART” as the key visual word in the book title;
The second emphasizes “CLIENT SERVICE” as the key visual words in the book title; and,
The third emphasizes just the word "CLIENT" in the book title.

A top-of-the-page is a pre-head that applies to all three versions:
“6 TIMELESS PRINCIPLES FOR ADVERTISING & MARKETING PRO’s
IN AN AI WORLD"

There's a mid-page sub-head for all three versions:
“THE CLASSIC GUIDE,” followed by
“FOURTH EDITION BY DENNIS HARTWELL

And there's a one-line, bottom-of-the-page designation:
“Foreword by Pam Kettering, Global Executive Creative Director, Bluefinch"

The pallette for the previously published third edition was black with red as an accent color on a field of white; I've attached a sample for reference, so you can see how it was executed. For this new fourth edition, I'd like to change the accent color from red to either Wedgewood blue, or British racing green, or an alternative that is assertive and color saturated -- think of primary colors -- that contrast sufficiently with the base of black. As an alternative, you can consider a cover that used either Wedgewood blue, British racing green, or another possibility as a full-bleed field, with copy content either revered out or surprinted.

Lastly, while the new cover largely is meant to be typographically driven, if you can come up with a visual metaphor that illustrates and builds on the book's title, that would be very helpful. By way of reference, the third edition's book cover attempted to do this by introducing a visual element at the end of the book's title that's meant to represent an artist's paint splatter (although I admit it didn't work as well as it should).

Target Market(s)

Prospective purchasers of the book who might discover copies at a bookstore, but more likely will encounter it through online distributors such as Vendora, Fitch & Marlow, and Tindle’s.

Industry/Entity Type

Advertising and marketing

Font styles to use
Serif
Sans Serif
Other font styles liked:
• A mix of serif and san-serif typefaces is okay. for the examples I shared, I relieid on "Arial Rounded Bold" but you need not be weeded to this. If you opt to mix in a serif font, I am partial to Cambria as a typeface.

Requirements
Must have
• To achieve the goal of being “connected with but distinct” from previous editions, the new cover should be:  Largely typographic, but displaying a color palette different from the previous editions’ black-plus-red-accent on a canvas of white.  Any new accent color selected for use should be vibrant, strong, and highly saturated; think “British racing green,” “Wedgewood blue,” or their equivalents.  In addition to a powerful, “billboard” approach to type and color, consider other visual metaphors that are likely to engage the readers. The winning cover design will stand out from other books, while connecting with the previously published third edition.
Nice to have
• If you can find way to illustrate the book's title through a visual metaphor, that would be ideal.a
Should not have
• Anything that is frivolous or non-sensical

```html
<!DOCTYPE html>
<html lang="en">
<head>
<meta charset="utf-8">
<title>The Craft of Patron Care — Fourth Edition Cover</title>
<link rel="stylesheet" href="https://fonts.googleapis.com/css2?family=Archivo:wght@400;500;700;800;900&display=swap">
<style>
  :root {
    --backdrop: #dadada;
    --paper: #ffffff;
    --racing-green: #003d3a;
  }
  * { margin: 0; padding: 0; box-sizing: border-box; }
  html, body {
    width: 1200px;
    height: 849px;
    overflow: hidden;
    background: var(--backdrop);
  }
  .stage {
    position: relative;
    width: 1200px;
    height: 849px;
  }
  .cover {
    position: absolute;
    left: 343px;
    top: 44px;
    width: 514px;
    height: 760px;
    background: var(--paper);
    color: var(--racing-green);
    font-family: "Archivo", Arial, sans-serif;
  }
  .prehead {
    position: absolute;
    top: 92px;
    left: 0;
    width: 100%;
    text-align: center;
    font-size: 10px;
    font-weight: 400;
    line-height: 15px;
    letter-spacing: 0.3px;
  }
  .title {
    position: absolute;
    top: 250px;
    left: 85px;
    width: 360px;
  }
  .title-lead {
    display: flex;
    align-items: flex-end;
    gap: 8px;
  }
  .title-the {
    writing-mode: vertical-rl;
    transform: rotate(180deg);
    font-size: 39px;
    font-weight: 800;
    line-height: 0.74;
    letter-spacing: -0.5px;
  }
  .title-key {
    font-size: 104px;
    font-weight: 900;
    line-height: 0.74;
    letter-spacing: -4px;
  }
  .title-rest {
    margin-top: 17px;
    font-size: 34px;
    font-weight: 800;
    line-height: 1;
    letter-spacing: 0.2px;
  }
  .edition {
    position: absolute;
    top: 418px;
    left: 0;
    width: 100%;
    text-align: center;
  }
  .edition-label {
    font-size: 21px;
    font-weight: 800;
    letter-spacing: 0.8px;
    line-height: 1;
  }
  .edition-author {
    margin-top: 9px;
    font-size: 14.5px;
    font-weight: 400;
    line-height: 1;
  }
  .foreword {
    position: absolute;
    top: 664px;
    left: 0;
    width: 100%;
    text-align: center;
    font-size: 10.5px;
    font-weight: 500;
    letter-spacing: 0.2px;
  }
</style>
</head>
<body>
  <main class="stage">
    <section class="cover" aria-label="Book cover">
      <p class="prehead">6 TIMELESS PRINCIPLES FOR<br>ADVERTISING &amp; MARKETING PRO’s IN AN AI WORLD</p>

      <h1 class="title">
        <span class="title-lead">
          <span class="title-the">THE</span>
          <span class="title-key">CRAFT</span>
        </span>
        <span class="title-rest" style="display:block">OF PATRON CARE</span>
      </h1>

      <div class="edition">
        <p class="edition-label">THE CLASSIC GUIDE</p>
        <p class="edition-author">FOURTH EDITION BY DENNIS HARTWELL</p>
      </div>

      <p class="foreword">Foreword by Pam Kettering, Global Executive Creative Director, Bluefinch</p>
    </section>
  </main>
</body>
</html>
```